The Larchmont Fitters

We need a business card design for our wardrobe company.
Please visit our website www.glimmerbayinteriors.com to get an idea of who we are.

```html
<!DOCTYPE html>
<html lang="en">
<head>
<meta charset="utf-8">
<title>The Larchmont Fitters – Business Card</title>
<link rel="stylesheet" href="https://fonts.googleapis.com/css2?family=Exo+2:wght@400;500&family=Montserrat:wght@500;600&display=swap">
<style>
  :root {
    --backdrop: #e9cf33;
    --card: #e6e6e6;
    --ink: #111111;
    --band: #000000;
    --accent: #a08b6a;
    --figure: #d2ccc2;
    --rule: #555555;
    --white: #ffffff;
  }
  * { margin: 0; padding: 0; box-sizing: border-box; }
  html, body { width: 1200px; height: 1199px; overflow: hidden; }
  body {
    background: var(--backdrop);
    position: relative;
    font-family: "Exo 2", sans-serif;
    color: var(--ink);
  }
  .card {
    position: absolute;
    left: 100px; top: 300px;
    width: 1000px; height: 600px;
    background: var(--card);
    overflow: hidden;
    box-shadow: 0 18px 40px rgba(0,0,0,0.18);
  }
  .brand-figure {
    position: absolute;
    left: 300px; top: 330px;
    width: 330px; height: 270px;
    background: radial-gradient(ellipse at 50% 50%, var(--figure) 0%, rgba(210,204,194,0.55) 50%, rgba(210,204,194,0) 72%);
  }
  .brand-mark {
    position: absolute;
    left: 70px; top: 90px;
    width: 200px; height: 200px;
    border: 7px solid var(--ink);
  }
  .company {
    position: absolute;
    left: 315px; top: 78px;
    font-family: "Montserrat", sans-serif;
    font-weight: 600;
    font-size: 36px;
    letter-spacing: 0.5px;
    text-transform: uppercase;
    white-space: nowrap;
  }
  .tagline {
    position: absolute;
    left: 400px; top: 140px;
    font-family: "Montserrat", sans-serif;
    font-weight: 500;
    font-size: 32px;
    white-space: nowrap;
  }
  .divider {
    position: absolute;
    left: 560px; top: 290px;
    width: 2px; height: 100px;
    background: var(--rule);
  }
  .contacts {
    position: absolute;
    left: 585px; top: 270px;
    list-style: none;
    font-size: 24px;
    line-height: 36px;
    white-space: nowrap;
  }
  .contacts li { display: flex; align-items: center; gap: 12px; }
  .contacts svg { width: 20px; height: 20px; flex: none; }
  .person {
    position: absolute;
    left: 235px; top: 395px;
  }
  .person .name {
    font-size: 48px;
    font-weight: 500;
    color: var(--accent);
    line-height: 1;
    white-space: nowrap;
  }
  .person .role {
    font-size: 20px;
    margin-top: 4px;
    white-space: nowrap;
  }
  .social {
    position: absolute;
    right: 60px; top: 440px;
    display: flex; gap: 10px;
  }
  .social span {
    width: 30px; height: 30px;
    background: var(--ink);
    border-radius: 6px;
  }
  .band {
    position: absolute;
    left: 0; top: 505px;
    width: 100%; height: 46px;
    background: var(--band);
    color: var(--white);
    font-size: 26px;
    line-height: 46px;
    padding-left: 330px;
    white-space: nowrap;
  }
</style>
</head>
<body>
  <section class="card" aria-label="Business card for The Larchmont Fitters">
    <div class="brand-figure" role="img" aria-label="Faint brand figure decoration"></div>

    <div class="brand-mark" aria-hidden="true"></div>
    <h1 class="company">The Larchmont Fitters</h1>
    <p class="tagline">Built Square, Hung True</p>

    <div class="divider"></div>
    <ul class="contacts">
      <li>
        <svg viewBox="0 0 20 20" aria-hidden="true"><path d="M5 2l3 4-2 2c1 2 3 4 5 5l2-2 4 3-2 3C9 17 3 11 2 5z" fill="none" stroke="#a08b6a" stroke-width="1.4"/></svg>
        0207 555 0148
      </li>
      <li>
        <svg viewBox="0 0 20 20" aria-hidden="true"><rect x="2" y="5" width="16" height="11" fill="#a08b6a"/><path d="M2 5l8 6 8-6" fill="none" stroke="#e6e6e6" stroke-width="1.4"/></svg>
        info@glimmerbayinteriors.com
      </li>
      <li>
        <svg viewBox="0 0 20 20" aria-hidden="true"><g fill="none" stroke="#a08b6a" stroke-width="1.3"><circle cx="10" cy="10" r="8"/><ellipse cx="10" cy="10" rx="3.5" ry="8"/><path d="M2 10h16M4 6h12M4 14h12"/></g></svg>
        www.glimmerbayinteriors.com
      </li>
    </ul>

    <div class="person">
      <p class="name">Tobias Hartley</p>
      <p class="role">Founder and Lead Fitting Designer</p>
    </div>

    <div class="social" aria-label="Social links">
      <span></span><span></span><span></span>
    </div>

    <p class="band">Alder Court, 42 Marlow Street, London EC2A 9QT</p>
  </section>
</body>
</html>
```